The Meridale Works
Buy+Sell+Repair & Take trade-ins. New & Used, All makes and models
24 Hours or so left in this contest. We have seen many good designs and a few of you are in contention as you have incorporated what we sell like GPS & Total stations etc which we like. We hope to get some even stronger options with our suggestions in mind in the closing hours but also the sooner the better. If we like your design but would simply like to make a small revision, we would like to give you time to correct prior to us picking another winner. Thanks for all your efforts.
draft #155 We like your creativity! Would like to see some new drafts from you soon showing some of the suggestions mentioned in previous posts. Maybe make the large earth and satellite more translucent. Put dots in between words like buy+sell etc instread of plus signs. Use icons to show quorvel, bramnet, phone, email and Valto then follow with proper info. Move everything around if need be to try to make look clean while having this info available. Look forward to new options from you. Thanks
#162 please make Icons & info larger.
#163 Can you move our logo & company name up a little & put buy, sell ect. just under it in the grey area.
Then put " Dealing in VORANT, MELDRIX, KAPUNO, FELSTOW, & ZIRVAN." in the blue area.
Note Please use period or comma instead of "+" on designs.
Project# 102,
I really like this one. Will you :
1) Take away the "box" from our names & put Names in upper corner, & put "Phone# & Email & address."
2) Keep our logo & company name as is.
3) Bottom left area put " Buy. Sell. Trade. Repair. New & Used. GPS. Robotics. Total Stations. Theodolites. & Levels "
4) Bottom Right area put "Bramnet, Valto, Quorvel, ect." (Please use "Icon" instead of words.)
5)To every one .... I would like to see the package deal after we get the card layout handled. ( I also like some of the ideas of the "swoosh" on the cars but don't know if the "info" will fit rite.
Thank you for your help.
Also please no highlight block over our names
Fifth but very important is that we are primarily an Internet based company and our Address is not really needed on our business card. Addreess could be removed but please include a second email address being dana@themeridaleworks.example to this card.
Fourth, Please keep with the concept I have seen on several designs that puts a translucent version of our globe logo on the opposite side of the darker logo. This more translucent globe can have our company contact info written on top of it as long as it still looks clean and the info is very clear to read.
Third, We like a small swoosh to seperate the card into two halves.
Second I very much need the card to have the logo and our name but then under that it should read Buy+Sell+Repair+Trade-in+New & Used+ All makes and Models. as seen in design #152
This should be a must!
Greeting all,
Sorry that I have not given much feedback yet but things are very busy. I have looked over the designs and have a few suggestions. First I will probably choose a design that gives the whole stationary and envelope options too.

```html
<!DOCTYPE html>
<html lang="en">
<head>
<meta charset="utf-8">
<title>The Meridale Works – Business Card</title>
<link href="https://fonts.googleapis.com/css2?family=Arimo:wght@400;700&display=swap" rel="stylesheet">
<style>
  :root {
    --backdrop: #e9e6e2;
    --card: #ffffff;
    --navy: #0d2350;
    --band-dark: #102c63;
    --band-mid: #3a6fb4;
    --band-light: #8fb4df;
    --text: #333a45;
    --muted: #5a6472;
    --icon-blue: #2a8fd6;
    --icon-navy: #1f5a96;
  }
  * { margin: 0; padding: 0; box-sizing: border-box; }
  html, body {
    width: 1200px; height: 780px; overflow: hidden;
    background: var(--backdrop);
    font-family: "Arimo", Arial, sans-serif;
  }
  .business-card {
    position: absolute; left: 60px; top: 80px;
    width: 1080px; height: 620px;
    background: var(--card);
    border-radius: 34px;
    box-shadow: 0 10px 30px rgba(0,0,0,.18);
    overflow: hidden;
  }
  .brand {
    position: absolute; left: 150px; top: 60px;
    display: flex; align-items: center; gap: 28px;
  }
  .brand-mark {
    flex: none;
    width: 190px; height: 190px; border-radius: 50%;
    background: radial-gradient(circle at 40% 35%, #5fa8e8, #1a4f9a 60%, #0b1f48);
  }
  .brand-text { display: flex; flex-direction: column; gap: 14px; }
  .brand-name {
    font-weight: 700; font-size: 54px; color: var(--navy);
    line-height: 1.05;
  }
  .services {
    font-size: 20px; line-height: 28px; color: var(--muted);
    max-width: 560px;
  }
  .divider-band {
    position: absolute; left: 0; right: 0; top: 322px; height: 34px;
    background: linear-gradient(90deg, var(--band-dark) 0%, var(--band-mid) 30%, var(--band-light) 50%, var(--band-mid) 72%, var(--band-dark) 100%);
    border-top: 2px solid #0a1d45; border-bottom: 2px solid #0a1d45;
  }
  .owners {
    position: absolute; right: 60px; top: 384px;
    color: var(--navy); font-weight: 700; font-size: 30px;
    letter-spacing: .3px;
  }
  .contact {
    position: absolute; left: 80px; right: 60px; top: 440px;
    color: var(--text); font-size: 24px; line-height: 46px;
  }
  .contact-row { display: flex; justify-content: flex-end; align-items: center; gap: 14px; white-space: nowrap; }
  .contact-row b { font-weight: 700; color: var(--navy); }
  .icon-dot { width: 24px; height: 24px; border-radius: 50%; background: var(--icon-blue); display: inline-block; }
  .icon-square { width: 24px; height: 24px; border-radius: 4px; background: var(--icon-navy); display: inline-block; }
</style>
</head>
<body>
  <div class="business-card">
    <div class="brand">
      <div class="brand-mark" role="img" aria-label="Globe emblem of The Meridale Works"></div>
      <div class="brand-text">
        <div class="brand-name">The Meridale Works</div>
        <div class="services">Buy. Sell. Repair. Trade-in. New &amp; Used. All makes and models.</div>
      </div>
    </div>

    <div class="divider-band"></div>

    <div class="owners">Owen &amp; Dana Halvorsen</div>

    <div class="contact">
      <div class="contact-row">
        <span><b>P:</b> (555) 382-7140</span>
        <span class="icon-dot"></span><span>the.meridale.works</span>
      </div>
      <div class="contact-row">
        <span><b>E:</b> owen@themeridaleworks.example <b>E:</b> dana@themeridaleworks.example</span>
      </div>
      <div class="contact-row">
        <span class="icon-dot"></span><span>Quorvel: @TheMeridaleWorks</span>
        <span class="icon-square"></span><span>pub/owen-halvorsen/41/207/c58</span>
      </div>
    </div>
  </div>
</body>
</html>
```